I need a simple infographic that describes the 4 basic elements of how to effectively create change.

The overall title (Gentle Pressure Relentlessly Applied) should be at the top of the infographic. Subtitle is: "Leading Change".
There are four steps:
1. Alignment- Agreement on Approach
2. Transparency- Metrics for Assurance
3. Skills- Training and Coaching
4. Integrity- Culture of Accountability

Target Market(s)

Business Leaders in a training workshop

Font styles to use
Serif

Requirements
Must have
• Here are the 4 elements of the Infographic: Please show them in order.
• 1. Agreement on Approach. (Alignment)
• 2. Metrics for Assurance (Transparency)
• 3. Training and Coaching (Skills)
• 4. Culture of Accountability (Integrity)
Nice to have
• Cool Graphics that depict the 4 steps.
Should not have
• Pictures.

```html
<!DOCTYPE html>
<html lang="en">
<head>
<meta charset="utf-8">
<title>Four Basic Elements of How to Effectively Create Change</title>
<link rel="stylesheet" href="https://fonts.googleapis.com/css2?family=Yanone+Kaffeesatz:wght@300&family=Raleway:wght@200;300&family=Roboto:wght@300&display=swap">
<style>
  :root {
    --header-blue: #3e627b;
    --header-shade: #2f5571;
    --title-pink: #f27fc0;
    --title-white: #ffffff;
    --green: #70fe8a;
    --row-1: #f1f5f4;
    --row-2: #e2fcef;
    --row-3: #c6fde6;
    --row-4: #b8fde2;
    --ink: #263f4d;
    --ink-soft: #466874;
    --target-red: #e8173a;
    --label: #1e2a30;
  }
  * { margin: 0; padding: 0; box-sizing: border-box; }
  html, body { width: 921px; height: 1200px; overflow: hidden; background: #fff; }
  .infographic { position: relative; width: 921px; height: 1200px; overflow: hidden; }

  .header { position: absolute; left: 0; top: 0; width: 921px; height: 342px; background: var(--header-blue); }
  .header-shade { position: absolute; left: 0; top: 0; }
  .header-title {
    position: absolute; left: 311px; top: 62px;
    font-family: "Yanone Kaffeesatz", sans-serif; font-weight: 300;
    font-size: 66px; line-height: 73px; color: var(--title-white);
    letter-spacing: 0.5px;
  }
  .header-title .accent { color: var(--title-pink); }

  .rows { position: absolute; left: 0; top: 342px; width: 921px; height: 858px; }
  .row { position: absolute; left: 0; width: 921px; box-shadow: 0 -3px 4px rgba(0,0,0,0.08); }
  .row-1 { top: 0; height: 196px; background: var(--row-1); box-shadow: none; }
  .row-2 { top: 196px; height: 218px; background: var(--row-2); }
  .row-3 { top: 414px; height: 212px; background: var(--row-3); }
  .row-4 { top: 626px; height: 232px; background: var(--row-4); }

  .row-label {
    position: absolute; right: 189px; text-align: right;
    font-family: "Roboto", sans-serif; font-weight: 300;
    font-size: 16.5px; line-height: 21px; color: var(--label);
  }
  .row-icon { position: absolute; left: 774px; }

  .green-wedge { position: absolute; left: 0; top: 342px; }

  .motto {
    position: absolute; left: 49px; top: 530px;
    font-family: "Raleway", sans-serif; font-weight: 200;
    font-size: 45px; line-height: 53px; color: #fff; letter-spacing: 0.5px;
  }
  .motto-sub {
    position: absolute; left: 48px; top: 694px;
    font-family: "Raleway", sans-serif; font-weight: 300;
    font-size: 15px; color: #fff; font-variant: small-caps; letter-spacing: 0.3px;
  }
</style>
</head>
<body>
<main class="infographic">
  <header class="header">
    <svg class="header-shade" width="280" height="342" aria-hidden="true">
      <polygon points="0,0 272,0 132,342 0,342" fill="var(--header-shade)"/>
    </svg>
    <h1 class="header-title">
      <span class="accent">FOUR BASIC</span> ELEMENTS<br>
      OF HOW TO EFFECTIVELY<br>
      <span class="accent">CREATE CHANGE</span>
    </h1>
  </header>

  <section class="rows">
    <div class="row row-1">
      <p class="row-label" style="top:81px">Agreement on Approach<br>(Alignment)</p>
      <svg class="row-icon" style="top:60px" width="116" height="100" viewBox="0 0 116 100" aria-hidden="true">
        <path d="M2 8 L30 20 L62 14 L86 22 L114 6 L114 56 L92 62 L66 88 C60 94 52 92 50 86 L40 92 C34 94 28 90 28 84 L20 78 L8 70 L2 60 Z" fill="var(--ink)"/>
        <path d="M46 24 L36 42 C34 48 42 50 46 46 L56 32 Z" fill="var(--row-1)"/>
        <circle cx="22" cy="68" r="7" fill="var(--ink)"/>
        <circle cx="32" cy="76" r="7" fill="var(--ink)"/>
        <circle cx="42" cy="84" r="7" fill="var(--ink)"/>
        <circle cx="52" cy="90" r="7" fill="var(--ink)"/>
        <path d="M58 60 L78 78 M64 52 L86 70 M72 46 L92 62" stroke="var(--row-1)" stroke-width="3" fill="none"/>
      </svg>
    </div>
    <div class="row row-2">
      <p class="row-label" style="top:113px">Metrics for Assurance<br>(Transparency)</p>
      <svg class="row-icon" style="top:62px" width="116" height="116" viewBox="0 0 116 116" aria-hidden="true">
        <line x1="10" y1="104" x2="40" y2="74" stroke="var(--ink)" stroke-width="16" stroke-linecap="round"/>
        <circle cx="70" cy="44" r="38" fill="var(--ink)"/>
        <circle cx="70" cy="44" r="29" fill="#fff"/>
        <path d="M74 24 A20 20 0 0 1 90 42" stroke="var(--ink-soft)" stroke-width="6" fill="none" opacity="0.7"/>
      </svg>
    </div>
    <div class="row row-3">
      <p class="row-label" style="top:117px">Training and Coaching<br>(Skills)</p>
      <svg class="row-icon" style="top:58px" width="116" height="106" viewBox="0 0 116 106" aria-hidden="true">
        <circle cx="50" cy="56" r="49" fill="var(--ink)"/>
        <circle cx="50" cy="56" r="39" fill="#fff"/>
        <circle cx="50" cy="56" r="31" fill="var(--target-red)"/>
        <circle cx="50" cy="56" r="21" fill="#fff"/>
        <circle cx="50" cy="56" r="12" fill="var(--ink)"/>
        <line x1="50" y1="56" x2="104" y2="12" stroke="var(--ink-soft)" stroke-width="3"/>
        <path d="M98 6 L100 16 L110 18 M104 2 L106 12 L114 12" stroke="var(--ink-soft)" stroke-width="3" fill="none"/>
      </svg>
    </div>
    <div class="row row-4">
      <p class="row-label" style="top:97px">Culture of Accountability<br>(Integrity)</p>
      <svg class="row-icon" style="top:50px" width="120" height="124" viewBox="0 0 120 124" aria-hidden="true">
        <circle cx="74" cy="28" r="27" fill="var(--ink-soft)"/>
        <path d="M44 110 L44 82 C44 66 56 56 74 56 C96 56 112 68 116 84 L116 110 Z" fill="var(--ink-soft)"/>
        <circle cx="38" cy="40" r="28" fill="var(--ink)" stroke="var(--row-4)" stroke-width="3"/>
        <path d="M2 122 L2 96 C2 80 16 68 38 68 C60 68 74 80 74 96 L74 122 Z" fill="var(--ink)" stroke="var(--row-4)" stroke-width="3"/>
      </svg>
    </div>
  </section>

  <svg class="green-wedge" width="530" height="858" aria-hidden="true">
    <polygon points="0,0 524,0 260,858 0,858" fill="var(--green)"/>
  </svg>
  <h2 class="motto">GENTLE PRESSURE<br>RELENTLESSLY<br>APPLIED</h2>
  <p class="motto-sub">“Leading Change”</p>
</main>
</body>
</html>
```